New Alcoholic Spiked Seltzer Line

We need a can design for a line of low calorie alcoholic seltzer. This product is a sparkling water and vodka drink with no sugar added in a slim 12 oz can.

This is a lighter, healthier, alternative to the sugary ready-to-drinks on the market. The product contains only 3 ingredients: Vodka, Water and Natural Flavors. It has only 100 calories but still has 5% alcohol, so you don't need to sacrifice alcohol to cut calories.

This product also does not contain any preservatives.

We want this design to communicate the following objectives to the consumer and in this order:

1. Appetizing product
2.Low calorie
3.Communicate the type of beverage (Spiked Seltzer)

The brand name of the product is VELKA.

The flavor of the product needed to be used for the design is Mango-Orange.

Comparable products are:

www.brisavelfizz.example/
https://www.tarnowbubble.example
https://quellrind.example/

The designs should not infringe or copy the creative directions of the products mentionned above. They are only given so that you can better understand the type of product we are developing.

Target Market(s)

Young Professional women between the ages of 25 and 44

Industry/Entity Type

Product

Colors

Designer to choose colors to be used in the design.

Requirements
Must have
• Design extendibility, meaning it can be adapted for other flavors.
• This is a new category in the market we are targeting, so consumers must easily be able to identify what type of product this is.

```html
<!DOCTYPE html>
<html lang="en">
<head>
<meta charset="utf-8">
<title>VELKA Spiked Seltzer – Mango/Orange Can Label</title>
<link rel="stylesheet" href="https://fonts.googleapis.com/css2?family=Jost:wght@400;500;600&display=swap">
<style>
  :root {
    --backdrop: #ededed;
    --label-white: #fbfbfb;
    --ink: #1c1c1c;
    --sunshine: #f3ea4a;
    --badge-yellow: #e4db3c;
    --bolt-yellow: #f0d21c;
    --art-tone-light: #f7f3d6;
    --art-tone-deep: #e9dc86;
  }
  * { margin: 0; padding: 0; box-sizing: border-box; }
  html, body {
    width: 1200px;
    height: 800px;
    overflow: hidden;
    background: var(--backdrop);
    font-family: "Jost", "Futura", sans-serif;
    color: var(--ink);
  }
  .canvas {
    position: relative;
    width: 1200px;
    height: 800px;
  }
  .can-label {
    position: absolute;
    left: 460px;
    top: 50px;
    width: 280px;
    height: 700px;
    background: var(--label-white);
    overflow: hidden;
  }
  .accent-band {
    position: absolute;
    inset: 0;
    width: 280px;
    height: 700px;
  }
  .calorie-callout {
    position: absolute;
    left: 58px;
    top: 82px;
    display: flex;
    align-items: center;
    gap: 4px;
    font-size: 16px;
    font-weight: 500;
    letter-spacing: 0.2px;
  }
  .calorie-callout svg { width: 16px; height: 30px; }
  .brand-name {
    position: absolute;
    left: 0;
    width: 100%;
    top: 262px;
    text-align: center;
    font-size: 48px;
    font-weight: 500;
    letter-spacing: 1px;
    line-height: 1;
  }
  .fruit-art {
    position: absolute;
    left: 86px;
    top: 326px;
    width: 112px;
    height: 110px;
    border-radius: 50%;
    background: radial-gradient(circle at 40% 40%, var(--art-tone-light), var(--art-tone-deep));
    opacity: 0.85;
  }
  .product-type {
    position: absolute;
    left: 0;
    width: 100%;
    top: 478px;
    text-align: center;
    font-size: 21px;
    font-weight: 400;
    letter-spacing: 0.3px;
  }
  .flavor-name {
    position: absolute;
    left: 0;
    width: 100%;
    top: 506px;
    text-align: center;
    font-size: 21px;
    font-weight: 600;
    letter-spacing: 0.3px;
  }
  .alcohol-line {
    position: absolute;
    left: 0;
    width: 100%;
    top: 624px;
    display: flex;
    justify-content: center;
    align-items: center;
    gap: 6px;
    font-size: 13px;
    font-weight: 400;
    letter-spacing: 0.5px;
  }
  .alcohol-badge {
    display: inline-flex;
    align-items: center;
    justify-content: center;
    width: 34px;
    height: 34px;
    border-radius: 50%;
    background: var(--badge-yellow);
    font-size: 17px;
    font-weight: 500;
  }
</style>
</head>
<body>
<main class="canvas">
  <section class="can-label">
    <svg class="accent-band" viewBox="0 0 280 700" aria-hidden="true">
      <polygon points="0,262 280,128 280,272 0,438" fill="var(--sunshine)"/>
    </svg>

    <p class="calorie-callout">
      <svg viewBox="0 0 16 30" aria-hidden="true">
        <polygon points="9,0 1,17 7,17 4,30 15,11 9,11 12,0" fill="var(--bolt-yellow)"/>
      </svg>
      100 calories
    </p>

    <h1 class="brand-name">VELKA</h1>

    <div class="fruit-art" role="img" aria-label="Line drawing of two mangoes with leaves"></div>

    <p class="product-type">SPIKED SELTZER</p>
    <p class="flavor-name">MANGO/ORANGE</p>

    <p class="alcohol-line">
      <span>•</span><span>ALC</span>
      <span class="alcohol-badge">5.0</span>
      <span>VOL</span><span>•</span>
    </p>
  </section>
</main>
</body>
</html>
```